I need to have a website created  for my company , Amber Wheels.  What we are selling is mini electric trucks . These mini electric trucks require no license
or insurance.  They only go 25 k/h and are considered to be electric  mobility covered  scooters .  So far i only have a dozen of these just to see how well they sell before i sink a bunch of money into other models , designs ect. I am submitting 5 or 6 pics of the model to be put on the website along with one pic containing the specs of  the model i am going to sell .  Amber Wheels is the name of the company with our catch phrase : Discover the liberty of an amber wheel.  The consumers i would like to target mostly are people who are unable to get a  drivers license .  It would give seniors who have had their license taken away for medical reasons,  age etc. Anyone who does not have the luxury of having a car  but still need to do life tasks like going to grocery store ,  dr appt  but have to rely on someone else to take them . This scooter gives them that freedom to get where they want whenever they want to keep their independence at an affordable price.  The web domain i already have is at www.amberwheels-demo.ca  i will also include a pic of my business cards that contains all the info of the company eg. Phone number , email etc. Thank you for you time and creativity

```html
<!DOCTYPE html>
<html lang="en">
<head>
<meta charset="utf-8">
<title>Amber Wheels — Mini Electric Trucks</title>
<link href="https://fonts.googleapis.com/css2?family=Montserrat:ital,wght@0,400;0,500;0,600;0,700;0,800;1,500&family=Yesteryear&display=swap" rel="stylesheet">
<style>
:root{
  --green:#3bbb8f;
  --teal:#2d7e6c;
  --teal-dark:#246a5b;
  --ink:#2b2b2b;
  --body:#555;
  --muted:#888;
  --soft:#f3f4f6;
  --footer:#232427;
  --star:#f5a623;
  --white:#fff;
}
*{box-sizing:border-box;margin:0;padding:0}
html,body{width:1200px;height:4662px;overflow:hidden}
body{position:relative;font-family:"Montserrat",sans-serif;color:var(--ink);background:var(--white)}
.abs{position:absolute}
.script{font-family:"Yesteryear",cursive;font-weight:400}
.kicker{display:flex;align-items:center;gap:14px;color:var(--teal);font-weight:700;font-size:22px;letter-spacing:-.3px;text-transform:uppercase}
.kicker::before{content:"";width:180px;height:2px;background:var(--teal)}
.center-head{position:absolute;left:0;width:1200px;text-align:center}
.center-head .kicker{justify-content:center}
.center-head .script{font-size:40px;color:var(--ink);margin-top:4px}
.btn{display:inline-flex;align-items:center;justify-content:space-between;gap:14px;background:var(--teal);color:#fff;font-size:13px;font-weight:600;text-transform:uppercase;border-radius:6px;padding:0 8px 0 14px;box-shadow:0 4px 0 rgba(0,0,0,.12)}
.btn .arr{width:30px;height:30px;border-radius:50%;background:#fff;display:flex;align-items:center;justify-content:center}
.circle-nav{width:56px;height:56px;border-radius:50%;border:1.5px solid currentColor;display:flex;align-items:center;justify-content:center}

/* hero */
.hero{left:0;top:0;width:1200px;height:770px;background:linear-gradient(180deg,#56646b 0%,#8e8a7c 22%,#d6a066 40%,#e0a464 47%,#5c5a55 53%,#4a4844 68%,#a8a8a6 86%,#fff 100%)}
.hero-truck{left:430px;top:210px;width:710px;height:460px;border-radius:40px;background:radial-gradient(ellipse at 50% 50%,rgba(235,238,240,.85),rgba(200,205,210,.35) 60%,rgba(0,0,0,0) 75%)}
.logo{color:#fff}
.logo .name{font-weight:700;font-size:38px;letter-spacing:-.5px}
.logo .tag{font-style:italic;font-weight:500;font-size:14px;margin-top:2px}
.nav{left:468px;top:48px;display:flex;gap:34px;color:#fff;font-size:12px;font-weight:600}
.nav .on{border-bottom:2px solid #fff;padding-bottom:8px}
.lets{left:986px;top:34px;width:104px;height:44px;border:1.5px solid #fff;border-radius:6px;color:#fff;font-size:12px;font-weight:700;display:flex;align-items:center;justify-content:center}
.hero-title{left:110px;top:262px;color:#fff;font-size:66px;font-weight:800;letter-spacing:-1px}
.hero-sub{left:112px;top:340px;color:#fff;font-size:22px;font-weight:500}

/* about */
.photo{background:linear-gradient(135deg,#8a7a6c,#c9b4a0 55%,#5f5a57)}
.frame{border:3px solid var(--teal)}
.about-text{left:622px;top:812px;width:480px}
.about-text .script{font-size:34px;line-height:46px;margin:14px 0 16px}
.about-text p{font-size:14px;line-height:26px;color:var(--body)}

/* products */
.products{left:0;top:1280px;width:1200px;height:742px;background:var(--green)}
.products .kicker,.products .script{color:#fff}
.products .kicker::before{background:#fff}
.card{background:#fff;width:308px}
.p-card{height:417px;top:188px;text-align:center}
.p-img{margin:32px auto 0;width:250px;height:170px;border-radius:6px;background:linear-gradient(180deg,#f1f3f4,#d9dde0)}
.p-card h3{font-size:22px;font-weight:600;margin-top:38px}
.p-card p{font-size:13px;line-height:22px;color:var(--body);margin:12px 22px 0}
.p-btns{display:flex;justify-content:center;gap:10px;margin-top:18px}
.ghost{height:42px;width:122px;border:1.5px solid #9a9a9a;border-radius:6px;font-size:12px;font-weight:500;display:flex;align-items:center;justify-content:center;color:#444}
.solid{height:42px;width:120px;border-radius:6px;background:var(--teal);color:#fff;font-size:12px;font-weight:600;display:flex;align-items:center;justify-content:center}
.dots{left:574px;top:645px;display:flex;gap:6px;align-items:center}
.dots i{width:11px;height:11px;border-radius:50%;border:1.5px solid #fff;display:block}
.dots i.on{width:15px;height:15px;background:#fff;box-shadow:inset 0 0 0 3px var(--green)}

/* specs */
.spec{display:flex;align-items:center;gap:18px}
.spec .ico{width:56px;height:56px;border-radius:50%;background:var(--teal);display:flex;align-items:center;justify-content:center;flex:none}
.spec small{display:block;font-size:12px;color:#555;text-transform:uppercase}
.spec b{display:block;font-size:20px;font-weight:500;color:var(--ink);margin-top:4px}
.spec.l{justify-content:flex-end;text-align:right;left:60px;width:300px}
.spec.r{left:804px;width:320px}
.spec-truck{left:410px;top:2280px;width:336px;height:232px;border-radius:12px;background:linear-gradient(180deg,#f4f5f6,#d5d9dc)}

/* testimonials */
.testi{left:0;top:2678px;width:1200px;height:575px;background:var(--soft)}
.t-card{top:210px;height:245px;text-align:center;box-shadow:0 2px 6px rgba(0,0,0,.06)}
.stars{margin-top:26px;display:flex;justify-content:center;gap:3px}
.t-card p{font-size:12.5px;line-height:22px;color:var(--body);margin:14px 24px 0}
.t-card h4{font-size:16px;font-weight:600;margin-top:18px;letter-spacing:.3px}
.t-card em{font-size:11px;color:var(--muted);display:block;margin-top:6px}
.tab{right:30px;bottom:-30px;width:60px;height:56px}
.t-arrow{color:#555;background:#fff}

/* blog */
.b-card{top:3452px;width:463px;height:480px;box-shadow:0 2px 10px rgba(0,0,0,.12)}
.b-img{height:248px;background:linear-gradient(135deg,#6b7f84,#b59674 50%,#3f4a52)}
.date{left:40px;top:20px;width:46px;height:76px;background:#fff;text-align:center;color:var(--teal);line-height:1}
.date b{display:block;font-size:32px;font-weight:500;padding-top:4px}
.date span{display:block;font-size:16px;font-weight:600}
.date small{display:block;font-size:11px;margin-top:2px}
.b-body{padding:18px 12px 0 12px}
.b-body h3{font-size:19px;line-height:28px;font-weight:600}
.b-body .meta{font-size:12.5px;color:var(--teal);margin-top:8px}
.b-body p{font-size:12.5px;line-height:22px;color:var(--body);margin-top:12px}
.outline{display:inline-flex;align-items:center;justify-content:center;width:154px;height:40px;border:1.5px solid var(--teal);border-radius:6px;color:var(--teal);font-size:13px;font-weight:600;margin-top:14px;box-shadow:0 3px 0 rgba(0,0,0,.08)}

/* footer */
.footer{left:0;top:4083px;width:1200px;height:579px;background:var(--footer);color:#fff}
.footer label{font-size:11px;font-weight:600;display:block;margin-bottom:8px;letter-spacing:.3px}
.field{width:262px;height:38px;background:#fff;border-radius:2px;color:#333;font-size:12px;display:flex;align-items:center;padding-left:10px}
.sub-btn{left:815px;top:158px;width:148px;height:42px;background:var(--teal);border-radius:6px;font-size:13px;font-weight:600;display:flex;align-items:center;justify-content:center}
.rule{left:112px;width:978px;height:1px;background:#4a4b4f}
.col h5{font-size:18px;font-weight:600;margin-bottom:22px}
.col li{list-style:none;font-size:11px;line-height:24px;text-transform:uppercase;font-weight:500}
.contact{display:flex;gap:12px;align-items:flex-start;margin-bottom:18px}
.contact .c-ico{width:30px;height:30px;border-radius:50%;background:#fff;display:flex;align-items:center;justify-content:center;flex:none}
.contact small{display:block;font-size:10px;color:#bbb}
.contact span{display:block;font-size:11px;line-height:14px}
.copy{font-size:11px}
.up{left:1120px;top:487px;width:42px;height:42px;border-radius:50%;background:var(--teal);display:flex;align-items:center;justify-content:center}
</style>
</head>
<body>

<!-- HERO -->
<section class="abs hero" role="img" aria-label="Mini electric truck parked on a beach at sunset"></section>
<div class="abs hero-truck" role="img" aria-label="White mini electric pickup truck with roof rack"></div>
<div class="abs logo" style="left:110px;top:26px">
  <div class="name">Amber Wheels</div>
  <div class="tag">Discover the liberty of an amber wheel.</div>
</div>
<nav class="abs nav">
  <span class="on">HOME</span><span>ABOUT US</span><span>OUR PRODUCTS</span><span>TESTIMONIALS</span><span>CONTACT US</span>
</nav>
<div class="abs lets">LETS TALK</div>
<h1 class="abs hero-title">AMBER WHEELS</h1>
<p class="abs hero-sub">Perspiciatis unde omnisiste natus error</p>
<div class="abs btn" style="left:112px;top:395px;height:42px;width:170px">Get Started<span class="arr"><svg width="14" height="14" viewBox="0 0 14 14"><path d="M2 7h10M8 3l4 4-4 4" stroke="#2d7e6c" stroke-width="1.6" fill="none"/></svg></span></div>
<div class="abs circle-nav" style="left:25px;top:335px;color:#fff"><svg width="18" height="18" viewBox="0 0 18 18"><path d="M15 9H3M7 5L3 9l4 4" stroke="#fff" stroke-width="1.6" fill="none"/></svg></div>
<div class="abs circle-nav" style="left:1118px;top:335px;color:#fff"><svg width="18" height="18" viewBox="0 0 18 18"><path d="M3 9h12M11 5l4 4-4 4" stroke="#fff" stroke-width="1.6" fill="none"/></svg></div>

<!-- ABOUT -->
<div class="abs frame" style="left:190px;top:845px;width:285px;height:308px"></div>
<div class="abs photo" style="left:123px;top:815px;width:187px;height:310px" role="img" aria-label="Smiling man at the wheel of a vehicle"></div>
<div class="abs photo" style="left:320px;top:892px;width:278px;height:300px;border:6px solid #fff;box-sizing:content-box;margin:-6px" role="img" aria-label="Smiling woman driving with her hands on the wheel"></div>
<div class="abs about-text">
  <div class="kicker">About Amber Wheels</div>
  <div class="script">Nemo enim ipsam voluptatem quia voluptas sit.</div>
  <p>Perspiciatis unde omnis iste natus error sit voluptatem accusantium doloremque laudantium, totam rem aperiam, eaque ipsa quae ab illo inventore veritatis et quasi architecto beatae vitae dicta sunt explicabo. Nemo enim ipsam voluptatem quia voluptas sit aspernatur aut odit aut fugit, sed quia consequuntur magni dolores eos.</p>
  <div class="btn" style="margin-top:22px;height:42px;width:170px">Learn More<span class="arr"><svg width="14" height="14" viewBox="0 0 14 14"><path d="M2 7h10M8 3l4 4-4 4" stroke="#2d7e6c" stroke-width="1.6" fill="none"/></svg></span></div>
</div>

<!-- PRODUCTS -->
<section class="abs products">
  <div class="center-head" style="top:80px"><div class="kicker">What We Have</div><div class="script">Our Products</div></div>
  <div class="abs card p-card" style="left:112px"><div class="p-img" role="img" aria-label="Mini electric truck, side view"></div><h3>Kansectetur Ladipisci</h3><p>Perspiciatis unde omnis iste natus error sit voluptatem accusantium.</p><div class="p-btns"><span class="ghost">VIEW DETAILS</span><span class="solid">FREE RIDE</span></div></div>
  <div class="abs card p-card" style="left:446px"><div class="p-img" role="img" aria-label="Mini electric truck, side profile"></div><h3>Kansectetur Ladipisci</h3><p>Perspiciatis unde omnis iste natus error sit voluptatem accusantium.</p><div class="p-btns"><span class="ghost">VIEW DETAILS</span><span class="solid">FREE RIDE</span></div></div>
  <div class="abs card p-card" style="left:780px"><div class="p-img" role="img" aria-label="Mini electric truck, front view"></div><h3>Kansectetur Ladipisci</h3><p>Perspiciatis unde omnis iste natus error sit voluptatem accusantium.</p><div class="p-btns"><span class="ghost">VIEW DETAILS</span><span class="solid">FREE RIDE</span></div></div>
  <div class="abs dots"><i></i><i class="on"></i><i></i></div>
</section>

<!-- PRODUCT DESCRIPTION -->
<div class="center-head" style="top:2100px"><div class="kicker">About Product</div><div class="script">Product Desciption</div></div>
<svg width="0" height="0" style="position:absolute"><defs>
<g id="ring"><circle cx="14" cy="14" r="10" fill="none" stroke="#fff" stroke-width="1.6"/><circle cx="14" cy="14" r="4" fill="none" stroke="#fff" stroke-width="1.6"/></g>
</defs></svg>
<div class="abs spec l" style="top:2207px"><div><small>Dimension</small><b>3500*1360*1680mm</b></div><span class="ico"><svg width="28" height="28" viewBox="0 0 28 28"><path d="M14 4l9 5v10l-9 5-9-5V9z M5 9l9 5 9-5 M14 14v10" fill="none" stroke="#fff" stroke-width="1.5"/></svg></span></div>
<div class="abs spec l" style="top:2289px"><div><small>Motor</small><b>1500w</b></div><span class="ico"><svg width="28" height="28" viewBox="0 0 28 28"><rect x="7" y="8" width="14" height="13" rx="2" fill="none" stroke="#fff" stroke-width="1.5"/><path d="M4 12h3M4 17h3M21 12h3M21 17h3M11 4v4M17 4v4" stroke="#fff" stroke-width="1.5"/></svg></span></div>
<div class="abs spec l" style="top:2372px"><div><small>Controller</small><b>24tubes</b></div><span class="ico"><svg width="28" height="28" viewBox="0 0 28 28"><use href="#ring"/></svg></span></div>
<div class="abs spec l" style="top:2454px"><div><small>Tyre</small><b>145vacuum</b></div><span class="ico"><svg width="28" height="28" viewBox="0 0 28 28"><circle cx="14" cy="14" r="10" fill="none" stroke="#fff" stroke-width="1.5"/><circle cx="14" cy="14" r="6" fill="none" stroke="#fff" stroke-width="1.5"/><circle cx="14" cy="14" r="2" fill="#fff"/></svg></span></div>
<div class="abs spec l" style="top:2535px"><div><small>Color</small><b>White</b></div><span class="ico"><svg width="28" height="28" viewBox="0 0 28 28"><path d="M8 5h8v18H8z M16 9l6 3-6 10" fill="none" stroke="#fff" stroke-width="1.5"/></svg></span></div>

<div class="abs spec-truck" role="img" aria-label="Mini electric truck, three-quarter front view"></div>

<div class="abs spec r" style="top:2207px"><span class="ico"><svg width="28" height="28" viewBox="0 0 28 28"><rect x="5" y="8" width="18" height="14" rx="1" fill="none" stroke="#fff" stroke-width="1.5"/><path d="M9 6v2M19 6v2M10 15h4M17 13v4M15 15h4" stroke="#fff" stroke-width="1.5"/></svg></span><div><small>Battery</small><b>60v50ah</b></div></div>
<div class="abs spec r" style="top:2289px"><span class="ico"><svg width="28" height="28" viewBox="0 0 28 28"><path d="M5 19a9 9 0 1 1 18 0" fill="none" stroke="#fff" stroke-width="1.5"/><path d="M14 19l5-6" stroke="#fff" stroke-width="1.6"/></svg></span><div><small>Max.Spped</small><b>35-45km/h</b></div></div>
<div class="abs spec r" style="top:2372px"><span class="ico"><svg width="28" height="28" viewBox="0 0 28 28"><use href="#ring"/></svg></span><div><small>Brake</small><b>Four-Wheel Disc Break</b></div></div>
<div class="abs spec r" style="top:2454px"><span class="ico"><svg width="28" height="28" viewBox="0 0 28 28"><path d="M11 4h6v7h7v6h-7v7h-6v-7H4v-6h7z" fill="none" stroke="#fff" stroke-width="1.5"/></svg></span><div><small>Drive Way</small><b>RWD</b></div></div>
<div class="abs spec r" style="top:2535px"><span class="ico"><svg width="28" height="28" viewBox="0 0 28 28"><rect x="7" y="5" width="12" height="18" rx="1" fill="none" stroke="#fff" stroke-width="1.5"/><path d="M14 9l-3 6h4l-3 5M19 12h3v7" fill="none" stroke="#fff" stroke-width="1.5"/></svg></span><div><small>Charging Time</small><b>7-10 Hours</b></div></div>

<!-- TESTIMONIALS -->
<section class="abs testi">
  <div class="center-head" style="top:80px"><div class="kicker">Testimonials</div><div class="script">What Our Customer's Say</div></div>
  <div class="abs circle-nav t-arrow" style="left:24px;top:322px"><svg width="18" height="18" viewBox="0 0 18 18"><path d="M15 9H3M7 5L3 9l4 4" stroke="#555" stroke-width="1.6" fill="none"/></svg></div>
  <div class="abs circle-nav t-arrow" style="left:1120px;top:322px"><svg width="18" height="18" viewBox="0 0 18 18"><path d="M3 9h12M11 5l4 4-4 4" stroke="#555" stroke-width="1.6" fill="none"/></svg></div>
</section>
<svg width="0" height="0" style="position:absolute"><defs><path id="star" d="M9 1l2.4 5 5.4.6-4 3.7 1.1 5.4L9 13l-4.9 2.7 1.1-5.4-4-3.7 5.4-.6z" fill="#f5a623"/></defs></svg>
<div class="abs card t-card" style="left:112px;top:2888px"><div class="stars"><svg width="18" height="18"><use href="#star"/></svg><svg width="18" height="18"><use href="#star"/></svg><svg width="18" height="18"><use href="#star"/></svg><svg width="18" height="18"><use href="#star"/></svg><svg width="18" height="18"><use href="#star"/></svg></div><p>Perspiciatis unde omnis istesenatus error sit voluptatem accusantium dolorelseijo mque laudantium totamkseo asorem aperiamdolores eos qui.</p><h4>MARTA QUELL</h4><em>- Orvane, CEO</em><svg class="abs tab" viewBox="0 0 60 56"><path d="M0 0h60v26L28 56V26H0z" fill="#fff"/><text x="12" y="26" font-family="Georgia,serif" font-size="40" font-weight="700" fill="#2d7e6c">“</text></svg></div>
<div class="abs card t-card" style="left:446px;top:2888px"><div class="stars"><svg width="18" height="18"><use href="#star"/></svg><svg width="18" height="18"><use href="#star"/></svg><svg width="18" height="18"><use href="#star"/></svg><svg width="18" height="18"><use href="#star"/></svg><svg width="18" height="18"><use href="#star"/></svg></div><p>Perspiciatis unde omnis istesenatus error sit voluptatem accusantium dolorelseijo mque laudantium totamkseo asorem aperiamdolores eos qui.</p><h4>MARTA QUELL</h4><em>- Orvane, CEO</em><svg class="abs tab" viewBox="0 0 60 56"><path d="M0 0h60v26L28 56V26H0z" fill="#fff"/><text x="12" y="26" font-family="Georgia,serif" font-size="40" font-weight="700" fill="#2d7e6c">“</text></svg></div>
<div class="abs card t-card" style="left:780px;top:2888px"><div class="stars"><svg width="18" height="18"><use href="#star"/></svg><svg width="18" height="18"><use href="#star"/></svg><svg width="18" height="18"><use href="#star"/></svg><svg width="18" height="18"><use href="#star"/></svg><svg width="18" height="18"><use href="#star"/></svg></div><p>Perspiciatis unde omnis istesenatus error sit voluptatem accusantium dolorelseijo mque laudantium totamkseo asorem aperiamdolores eos qui.</p><h4>MARTA QUELL</h4><em>- Orvane, CEO</em><svg class="abs tab" viewBox="0 0 60 56"><path d="M0 0h60v26L28 56V26H0z" fill="#fff"/><text x="12" y="26" font-family="Georgia,serif" font-size="40" font-weight="700" fill="#2d7e6c">“</text></svg></div>

<!-- BLOG -->
<div class="center-head" style="top:3335px"><div class="kicker">Amber Wheels Details</div><div class="script">Latest News and Blogs</div></div>
<article class="abs card b-card" style="left:110px">
  <div class="b-img" role="img" aria-label="Smiling driver behind the wheel of an open vehicle"></div>
  <div class="abs date"><b>21</b><span>FEB</span><small>2022</small></div>
  <div class="b-body"><h3>Perspiciatis unde omnis iste natus error sit voluptatem accusantium.</h3><div class="meta">12 comments &nbsp;|&nbsp; by Tobin Garrow</div><p>Perspiciatis unde omnis istesenatus error sit voluptatem accusantium dolorelseijo mque laudantium totamkseo asorem aperiamdolores eos qui.</p><span class="outline">MORE INFO</span></div>
</article>
<article class="abs card b-card" style="left:626px">
  <div class="b-img" role="img" aria-label="Friends taking photos from an open vehicle on a road trip"></div>
  <div class="abs date"><b>21</b><span>FEB</span><small>2022</small></div>
  <div class="b-body"><h3>Perspiciatis unde omnis iste natus error sit voluptatem accusantium.</h3><div class="meta">12 comments &nbsp;|&nbsp; by Tobin Garrow</div><p>Perspiciatis unde omnis istesenatus error sit voluptatem accusantium dolorelseijo mque laudantium totamkseo asorem aperiamdolores eos qui.</p><span class="outline">MORE INFO</span></div>
</article>
<div class="abs btn" style="left:525px;top:3962px;height:42px;width:150px">View More<span class="arr"><svg width="14" height="14" viewBox="0 0 14 14"><path d="M2 7h10M8 3l4 4-4 4" stroke="#2d7e6c" stroke-width="1.6" fill="none"/></svg></span></div>

<!-- FOOTER -->
<footer class="abs footer">
  <div class="abs script" style="left:0;width:1200px;text-align:center;top:55px;font-size:38px">Sign Up TO The Newsletter Today</div>
  <div class="abs" style="left:235px;top:140px"><label>NAME</label><div class="field">Tobin Garrow</div></div>
  <div class="abs" style="left:524px;top:140px"><label>EMAIL ADDRESS</label><div class="field">tobin.garrow@example.com</div></div>
  <div class="abs sub-btn">SUBSCRIBE</div>
  <div class="abs rule" style="top:270px"></div>

  <div class="abs logo" style="left:123px;top:335px"><div class="name">Amber Wheels</div><div class="tag">Discover the liberty of an amber wheel.</div></div>

  <div class="abs col" style="left:458px;top:300px"><h5>QUICK LINKS</h5><ul><li>Home</li><li>About Us</li><li>Products</li><li>Testimonials</li><li>FAQs</li><li>Contact Us</li></ul></div>
  <div class="abs col" style="left:670px;top:300px"><h5>OUR POLICIES</h5><ul><li>Terms &amp; Conditions</li><li>Privacy Policy</li><li>Company Values</li><li>Corporate Ethics Policy</li><li>Anti Slavery Policy</li><li>Contact</li></ul></div>
  <div class="abs col" style="left:918px;top:300px;width:180px"><h5>CONTACT US</h5>
    <div class="contact"><span class="c-ico"><svg width="14" height="14" viewBox="0 0 14 14"><path d="M7 1a4 4 0 0 1 4 4c0 3-4 8-4 8S3 8 3 5a4 4 0 0 1 4-4z" fill="#232427"/><circle cx="7" cy="5" r="1.4" fill="#fff"/></svg></span><div><small>Address</small><span>48 Larkspur Lane, Fenwick, ON, Canada K0L 2P0</span></div></div>
    <div class="contact"><span class="c-ico"><svg width="14" height="14" viewBox="0 0 14 14"><path d="M3 1l2.5 3-1.4 1.4a8 8 0 0 0 4.5 4.5L10 8.5l3 2.5-1.5 2C6 13 1 8 1 2.5z" fill="#232427"/></svg></span><div><small>Call Us</small><span>+1 (555) 014 2290</span></div></div>
    <div class="contact"><span class="c-ico"><svg width="14" height="14" viewBox="0 0 14 14"><rect x="1.5" y="3" width="11" height="8" fill="#232427"/><path d="M1.5 3l5.5 4.5L12.5 3" stroke="#fff" stroke-width="1" fill="none"/></svg></span><div><small>Email</small><span>hello@amberwheels-demo.ca</span></div></div>
  </div>

  <div class="abs up"><svg width="14" height="14" viewBox="0 0 14 14"><path d="M3 9l4-4 4 4" stroke="#fff" stroke-width="1.8" fill="none"/></svg></div>
  <div class="abs rule" style="top:512px"></div>
  <div class="abs copy" style="left:120px;top:537px">Copyright © 2022 | All Rights Reserved</div>
  <div class="abs copy" style="left:808px;top:537px">TERMS &amp; CONDITIONS &nbsp;&nbsp;&nbsp;&nbsp; | &nbsp;&nbsp;&nbsp;&nbsp; PRIVACY POLICY</div>
</footer>

</body>
</html>
```